The Steadfast Compass Method

I need an info graphic that shows how 7 habits help women in senior leadership to Honor Roots, Steady Mind, and Define Voice - leading to an increased power to influence

https://clipvarn.tv/Qm7RxPz2KaL

7 habits are;

Fearless Candour
Renewing Our Strength
Returning To Your Faith
Restoring Balance
Rethinking
Presence Shaping
Giving Regard

My Colours are GOLD - BFA55E
White & Black

Fonts Playfair Display & Raleway

The style and feel should be 'high end' luxury quality corporate

Style - luxury

Target Market(s)

Women in senior leadership

Industry/Entity Type

Leadership

Font styles to use
Serif
Sans Serif

Colors
fece3e
fee18a

Requirements
Must have
• style
elegance
contemporary feel
use gold, #BFA55E - black and white creatively

Nice to have
• unusual

```html
<!DOCTYPE html>
<html lang="en">
<head>
<meta charset="utf-8">
<title>The Steadfast Compass Method</title>
<link rel="stylesheet" href="https://fonts.googleapis.com/css2?family=Open+Sans:wght@700;800&family=Playfair+Display:wght@900&family=Raleway:wght@400;500&display=swap">
<style>
  :root {
    --gold: #bfa55e;
    --gold-light: #efe3c3;
    --gold-warm: #e3c87f;
    --gold-deep: #c3a55f;
    --venn-fill: #4a412d;
    --venn-line: #a8905a;
    --ink: #1a1509;
    --white: #ffffff;
    --cream: #f4efe2;
    --bg-dark: #111111;
    --bg-soft: #262626;
  }
  * { margin: 0; padding: 0; box-sizing: border-box; }
  html, body { width: 1200px; height: 927px; overflow: hidden; }
  body {
    position: relative;
    background: radial-gradient(ellipse at 20% 95%, var(--bg-soft) 0%, var(--bg-dark) 70%);
  }
  .frame {
    position: absolute;
    left: 57px; top: 59px; width: 1088px; height: 809px;
    border: 1.5px solid var(--gold);
    box-shadow: 0 -2px 18px -8px rgba(239, 227, 195, 0.35), 0 2px 18px -8px rgba(239, 227, 195, 0.35);
  }
  .title {
    position: absolute;
    left: 0; right: 0; top: 107px;
    text-align: center;
    font-family: "Open Sans", Arial, sans-serif;
    font-weight: 800;
    font-size: 49px;
    line-height: 50px;
    letter-spacing: 1px;
    color: var(--white);
  }
  .diagram { position: absolute; left: 0; top: 0; width: 1200px; height: 927px; }
  .habit { fill: url(#goldSheen); }
  .habit-label {
    font-family: "Playfair Display", Georgia, serif;
    font-weight: 900;
    font-size: 40px;
    fill: var(--ink);
    text-anchor: middle;
  }
  .venn-circle { fill: var(--venn-fill); }
  .venn-outline { fill: none; stroke: var(--venn-line); stroke-width: 3; }
  .venn-core { fill: url(#coreGlow); }
  .venn-label {
    font-family: "Raleway", Arial, sans-serif;
    font-weight: 500;
    fill: var(--cream);
    text-anchor: middle;
  }
  .core-label {
    font-family: "Raleway", Arial, sans-serif;
    font-weight: 500;
    font-size: 44px;
    fill: #2a2416;
    text-anchor: middle;
  }
</style>
</head>
<body>
  <div class="frame"></div>
  <h1 class="title">THE STEADFAST COMPASS METHOD</h1>

  <svg class="diagram" viewBox="0 0 2184 1687" xmlns="http://www.w3.org/2000/svg">
    <defs>
      <linearGradient id="goldSheen" x1="0" y1="0" x2="1" y2="0.35">
        <stop offset="0" stop-color="#e3c87f"/>
        <stop offset="0.45" stop-color="#efe3c3"/>
        <stop offset="0.75" stop-color="#dcc48e"/>
        <stop offset="1" stop-color="#c3a55f"/>
      </linearGradient>
      <linearGradient id="coreGlow" x1="0" y1="0" x2="0" y2="1">
        <stop offset="0" stop-color="#e3c87f"/>
        <stop offset="1" stop-color="#f0e4c4"/>
      </linearGradient>
      <clipPath id="clipLeft"><circle cx="1015" cy="683" r="222"/></clipPath>
      <clipPath id="clipRight"><circle cx="1248" cy="683" r="222"/></clipPath>
    </defs>

    <g class="habit-ring">
      <path class="habit" d="M481.4 496.2 A710 710 0 0 0 423.9 859.2 L669.5 833.4 A463 463 0 0 1 707.1 596.7 Z"/>
      <path class="habit" d="M428.7 896 A710 710 0 0 0 578.3 1231.8 L770.2 1076.4 A463 463 0 0 1 672.7 857.4 Z"/>
      <path class="habit" d="M602.4 1260.1 A710 710 0 0 0 910.6 1460.3 L986.9 1225.4 A463 463 0 0 1 785.9 1094.8 Z"/>
      <path class="habit" d="M946.3 1470.8 A710 710 0 0 0 1313.7 1470.8 L1249.8 1232.2 A463 463 0 0 1 1010.2 1232.2 Z"/>
      <path class="habit" d="M1349.4 1460.3 A710 710 0 0 0 1657.6 1260.1 L1474.1 1094.8 A463 463 0 0 1 1273.1 1225.4 Z"/>
      <path class="habit" d="M1681.7 1231.8 A710 710 0 0 0 1831.3 896 L1587.3 857.4 A463 463 0 0 1 1489.8 1076.4 Z"/>
      <path class="habit" d="M1836.1 859.2 A710 710 0 0 0 1778.6 496.2 L1552.9 596.7 A463 463 0 0 1 1590.5 833.4 Z"/>

      <text class="habit-label"><tspan x="540" y="702">Fearless</tspan><tspan x="545" y="749">Candour</tspan></text>
      <text class="habit-label"><tspan x="576" y="998">Renewing</tspan><tspan x="580" y="1045">Our</tspan><tspan x="602" y="1092">Strength</tspan></text>
      <text class="habit-label"><tspan x="800" y="1260">Returning</tspan><tspan x="822" y="1307">To</tspan><tspan x="835" y="1354">Your Faith</tspan></text>
      <text class="habit-label"><tspan x="1130" y="1360">Restoring</tspan><tspan x="1132" y="1407">Balance</tspan></text>
      <text class="habit-label"><tspan x="1450" y="1297">Rethinking</tspan></text>
      <text class="habit-label"><tspan x="1672" y="997">Presence</tspan><tspan x="1668" y="1044">Shaping</tspan></text>
      <text class="habit-label"><tspan x="1708" y="688">Giving</tspan><tspan x="1708" y="734">Regard</tspan></text>
    </g>

    <g class="venn">
      <circle class="venn-circle" cx="1015" cy="683" r="222"/>
      <circle class="venn-circle" cx="1248" cy="683" r="222"/>
      <circle class="venn-circle" cx="1130" cy="890" r="222"/>
      <g clip-path="url(#clipLeft)">
        <g clip-path="url(#clipRight)">
          <circle class="venn-core" cx="1130" cy="890" r="222"/>
        </g>
      </g>
      <circle class="venn-outline" cx="1015" cy="683" r="222"/>
      <circle class="venn-outline" cx="1248" cy="683" r="222"/>
      <circle class="venn-outline" cx="1130" cy="890" r="222"/>

      <text class="venn-label" font-size="48"><tspan x="914" y="623">Honor</tspan><tspan x="908" y="679">Roots</tspan></text>
      <text class="venn-label" font-size="54"><tspan x="1343" y="641">Define</tspan><tspan x="1348" y="704">Voice</tspan></text>
      <text class="venn-label" font-size="54"><tspan x="1133" y="981">Steady</tspan><tspan x="1140" y="1044">Mind</tspan></text>
      <text class="core-label" x="1133" y="746">IMPACT</text>
    </g>
  </svg>
</body>
</html>
```